Tern Hollow Acres Packaging Cannabis organic family legal farm Brand start

Industry/Entity Type

Cannabis, flower. pre rolls, distillate

Colors
0054AA
0677BA
7BADD7
CADEEF
E8F1F8

Requirements
Must have
• See attachment
Nice to have
• See attachment

```html
<!DOCTYPE html>
<html lang="en">
<head>
<meta charset="utf-8">
<title>Tern Hollow Acres – Pouch Packaging</title>
<link rel="stylesheet" href="https://fonts.googleapis.com/css2?family=Cinzel:wght@400&family=Arimo:wght@700&family=Raleway:wght@300&display=swap">
<style>
  :root{
    --stage:#e6e7e8;
    --ink:#050607;
    --gold:#d9b46a;
    --gold-deep:#8a6a2e;
    --blue-900:#0054AA;
    --blue-700:#0677BA;
    --blue-400:#7BADD7;
    --blue-200:#CADEEF;
    --blue-50:#E8F1F8;
    --die:#c21e1e;
    --die-text:#7a1e1e;
    --band:#4a1414;
    --clear:#dfa3cc;
    --matte:#f2e71d;
    --gloss:#7e4fa3;
    --unprinted:#d4d4d4;
  }
  *{box-sizing:border-box;margin:0;padding:0}
  html,body{width:1200px;height:2179px;overflow:hidden;background:var(--ink)}
  .canvas{position:relative;width:1200px;height:2179px;overflow:hidden;background:var(--ink)}
  .stage{position:absolute;left:0;top:0;width:1200px;height:793px;background:linear-gradient(180deg,#eeeff0 0%,var(--stage) 100%)}
  .pouch{position:absolute;top:134px;width:347px;height:530px;background:var(--ink);overflow:hidden;box-shadow:0 24px 40px rgba(0,0,0,.18)}
  .pouch--front{left:224px}
  .pouch--back{left:639px}

  .forest{position:absolute;background:
      radial-gradient(ellipse 30% 45% at 2% 55%,rgba(123,173,215,.55),rgba(123,173,215,0)),
      linear-gradient(180deg,rgba(5,6,7,0) 0%,rgba(138,106,46,.55) 14%,rgba(217,180,106,.75) 26%,var(--blue-50) 42%,var(--blue-200) 54%,var(--blue-400) 66%,#35506e 78%,#101a24 90%,var(--ink) 100%)}
  .pouch .forest{left:0;top:296px;width:100%;height:200px}

  .brand{position:absolute;left:0;width:100%;text-align:center;font-family:"Cinzel",serif;font-weight:400;color:var(--gold);white-space:nowrap}
  .tagline{position:absolute;left:0;width:100%;text-align:center;font-family:"Cinzel",serif;color:var(--gold);letter-spacing:.5px;white-space:nowrap}
  .pouch .brand{top:160px;font-size:16px}
  .pouch .tagline{top:210px;font-size:16px}
  .symbol-badge{position:absolute;background:#fff;border-radius:5px}
  .pouch .symbol-badge{left:283px;top:425px;width:33px;height:32px;background:#d8d8d8}
  .label-slot{position:absolute;border-radius:14px;display:flex;align-items:center;justify-content:center;text-align:center;font-family:"Raleway",sans-serif;font-weight:300;color:#222;line-height:1.24}
  .pouch .label-slot{left:96px;top:128px;width:166px;height:167px;font-size:15px;background:linear-gradient(135deg,#f7f7f7 0%,#dcdcdc 45%,#fafafa 70%,#cfcfcf 100%)}
  .glow{position:absolute;left:0;width:100%;background:linear-gradient(180deg,rgba(5,6,7,0),rgba(60,38,14,.7))}

  .art{position:absolute;top:954px;width:421px;height:712px}
  .art--front{left:103px}
  .art--back{left:671px}
  .art .glow{top:250px;height:110px}
  .art .forest{left:0;top:350px;width:421px;height:210px}
  .art .brand{top:195px;font-size:18px}
  .art .tagline{top:252px;font-size:19px}
  .clear-window{position:absolute;left:166px;top:293px;width:104px;height:104px;border-radius:50%;background:var(--clear);display:flex;align-items:center;justify-content:center;font-family:"Arimo",sans-serif;font-weight:700;font-size:11px;color:#111;z-index:2}
  .art .symbol-badge{left:338px;top:503px;width:38px;height:37px}
  .art .label-slot{left:122px;top:159px;width:194px;height:194px;font-size:18px;background:#fff}

  .dieline{position:absolute;left:0;top:0;width:1200px;height:2179px}
  .dim{font-family:"Arimo",sans-serif;font-weight:700;fill:var(--die-text)}
  .band-text{font-family:"Arimo",sans-serif;font-weight:700;font-size:27px;fill:#8a2a2a}

  .legend{position:absolute;top:1954px;left:687px;display:flex;gap:20px;list-style:none}
  .legend-item{width:74px;text-align:center;font-family:"Raleway",sans-serif;font-weight:300;font-size:15px;line-height:1.4;color:#3a3a3a}
  .swatch{width:74px;height:74px;border:3px solid #2a2a2a;margin-bottom:14px}
</style>
</head>
<body>
<main class="canvas">
  <section class="stage">
    <div class="pouch pouch--front">
      <p class="brand">Tern Hollow Acres</p>
      <p class="tagline">PREMIUM &amp; ORGANIC</p>
      <div class="forest" role="img" aria-label="Pine forest silhouette in gold, white and blue"></div>
      <div class="symbol-badge" role="img" aria-label="Regulatory symbol badge"></div>
    </div>
    <div class="pouch pouch--back">
      <div class="label-slot">CANNABIS<br>SIGN<br>LABEL<br>2"X2"<br>HERE</div>
      <div class="forest" role="img" aria-label="Pine forest silhouette in gold, white and blue"></div>
    </div>
  </section>

  <div class="art art--front">
    <div class="glow"></div>
    <p class="brand">Tern Hollow Acres</p>
    <p class="tagline">PREMIUM &amp; ORGANIC</p>
    <div class="clear-window">TRANSPARENT</div>
    <div class="forest" role="img" aria-label="Pine forest silhouette in gold, white and blue"></div>
    <div class="symbol-badge" role="img" aria-label="Regulatory symbol badge"></div>
  </div>
  <div class="art art--back">
    <div class="glow"></div>
    <div class="label-slot">CANNABIS<br>SIGN<br>LABEL<br>2"X2"<br>HERE</div>
    <div class="forest" role="img" aria-label="Pine forest silhouette in gold, white and blue"></div>
  </div>

  <svg class="dieline" viewBox="0 0 1200 2179" aria-hidden="true">
    <defs>
      <g id="pouch-panel" fill="none" stroke="var(--die)" stroke-width="1.3">
        <line x1="117" y1="941" x2="524" y2="941"/>
        <path d="M117 941l16-5v10zM524 941l-16-5v10z" fill="var(--die)"/>
        <line x1="117" y1="928" x2="117" y2="954"/>
        <line x1="524" y1="928" x2="524" y2="954"/>
        <rect x="117" y="954" width="407" height="712"/>
        <line x1="104" y1="954" x2="104" y2="1666"/>
        <path d="M104 954l-5 16h10zM104 1666l-5-16h10z" fill="var(--die)"/>
        <line x1="92" y1="954" x2="117" y2="954"/>
        <line x1="92" y1="1666" x2="117" y2="1666"/>
        <line x1="117" y1="1049" x2="524" y2="1049"/>
        <line x1="117" y1="1100" x2="524" y2="1100"/>
        <g stroke-dasharray="9 7">
          <line x1="117" y1="1066" x2="524" y2="1066"/>
          <line x1="117" y1="1083" x2="524" y2="1083"/>
          <line x1="146" y1="964" x2="146" y2="1637"/>
          <line x1="495" y1="964" x2="495" y2="1637"/>
          <line x1="104" y1="1514" x2="548" y2="1514"/>
          <path d="M148 1526Q190 1637 321 1637Q452 1637 493 1526"/>
          <line x1="150" y1="1637" x2="495" y2="1637"/>
        </g>
        <circle cx="321" cy="985" r="12" fill="#5a1212" stroke="none"/>
        <line x1="345" y1="962" x2="345" y2="985"/>
        <path d="M345 962l-3 7h6zM345 985l-3-7h6z" fill="var(--die)"/>
        <path d="M117 1007l18 6-18 6zM524 1007l-18 6 18 6z" fill="#5a1212"/>
        <line x1="537" y1="956" x2="537" y2="1010"/>
        <line x1="562" y1="956" x2="562" y2="1074"/>
        <line x1="527" y1="1074" x2="572" y2="1074"/>
        <line x1="537" y1="1514" x2="537" y2="1666"/>
        <line x1="524" y1="1666" x2="548" y2="1666"/>
      </g>
      <g id="pouch-labels" class="dim">
        <text x="321" y="926" font-size="27" text-anchor="middle">101.6 mm</text>
        <text transform="translate(90 1310) rotate(-90)" font-size="29" text-anchor="middle">177.8 mm</text>
        <text x="355" y="975" font-size="13">8 mm</text>
        <text transform="translate(545 983) rotate(90)" font-size="13" text-anchor="middle">15 mm</text>
        <text transform="translate(570 1015) rotate(90)" font-size="13" text-anchor="middle">30 mm</text>
        <text transform="translate(545 1590) rotate(90)" font-size="13" text-anchor="middle">38.1 mm</text>
        <text transform="translate(136 1310) rotate(-90)" font-size="12" text-anchor="middle">7.5 mm</text>
        <text transform="translate(513 1310) rotate(-90)" font-size="12" text-anchor="middle">7.5 mm</text>
        <text x="321" y="1657" font-size="13" text-anchor="middle">7.5 mm</text>
      </g>
    </defs>

    <rect x="48" y="854" width="544" height="27" fill="var(--band)"/>
    <text class="band-text" x="65" y="878">FRONT</text>
    <text class="band-text" x="343" y="878" text-anchor="middle">(OPENING)</text>
    <text class="band-text" x="577" y="878" text-anchor="end">TOP</text>
    <rect x="617" y="854" width="544" height="27" fill="var(--band)"/>
    <text class="band-text" x="634" y="878">BACK</text>
    <text class="band-text" x="912" y="878" text-anchor="middle">(OPENING)</text>
    <text class="band-text" x="1146" y="878" text-anchor="end">TOP</text>

    <use href="#pouch-panel"/>
    <use href="#pouch-labels"/>
    <use href="#pouch-panel" transform="translate(568 0)"/>
    <use href="#pouch-labels" transform="translate(568 0)"/>

    <rect x="48" y="1730" width="544" height="27" fill="var(--band)"/>
    <text class="band-text" x="65" y="1754">BOTTOM</text>
    <text class="band-text" x="577" y="1754" text-anchor="end">GUSSET</text>

    <g fill="none" stroke="var(--die)" stroke-width="1.3">
      <rect x="117" y="1830" width="407" height="304"/>
      <line x1="104" y1="1830" x2="104" y2="2134"/>
      <path d="M104 1830l-5 16h10zM104 2134l-5-16h10z" fill="var(--die)"/>
      <line x1="92" y1="1830" x2="117" y2="1830"/>
      <line x1="92" y1="2134" x2="117" y2="2134"/>
      <line x1="537" y1="1830" x2="537" y2="1982"/>
      <line x1="524" y1="1982" x2="548" y2="1982"/>
      <g stroke-dasharray="9 7">
        <rect x="146" y="1859" width="349" height="245"/>
        <ellipse cx="321" cy="1982" rx="175" ry="122"/>
        <line x1="117" y1="1982" x2="524" y2="1982"/>
      </g>
    </g>
    <g class="dim">
      <text transform="translate(90 1982) rotate(-90)" font-size="29" text-anchor="middle">76.2 mm</text>
      <text x="321" y="1846" font-size="13" text-anchor="middle">7.5 mm</text>
      <text x="321" y="2123" font-size="13" text-anchor="middle">7.5 mm</text>
      <text transform="translate(545 1915) rotate(90)" font-size="13" text-anchor="middle">38.1 mm</text>
      <text transform="translate(134 1982) rotate(-90)" font-size="12" text-anchor="middle">7.5 mm</text>
      <text transform="translate(513 1982) rotate(-90)" font-size="12" text-anchor="middle">7.5 mm</text>
    </g>
  </svg>

  <ul class="legend">
    <li class="legend-item"><div class="swatch" style="background:#ec1c24"></div>Die line (Does not Print)</li>
    <li class="legend-item"><div class="swatch" style="background:var(--unprinted)"></div>Unprinted Material</li>
    <li class="legend-item"><div class="swatch" style="background:var(--clear)"></div>Clear Unprinted Material</li>
    <li class="legend-item"><div class="swatch" style="background:var(--matte)"></div>Matte Areas</li>
    <li class="legend-item"><div class="swatch" style="background:var(--gloss)"></div>Gloss Areas</li>
  </ul>
</main>
</body>
</html>
```